Brix2Key Header

I want a professional Letterhead for my law firm. I'm attaching the letterhead I currently use in Word and PDF form. I'm also attaching my logo, and an example header that I like.

```html
<!DOCTYPE html>
<html lang="en">
<head>
<meta charset="utf-8">
<title>Brix2Key Letterhead</title>
<link rel="stylesheet" href="https://fonts.googleapis.com/css2?family=Montserrat:wght@400;600;800&family=Pinyon+Script&family=Tinos:ital@0;1&display=swap">
<style>
  :root {
    --backdrop: #d9d6d2;
    --paper: #f0f0f0;
    --ink: #4a4a4a;
    --ink-dark: #3b3c3e;
    --brand-green: #4a7c47;
    --brand-blue: #1d64a8;
    --icon-cyan: #1ea0d6;
    --sign-blue: #2350c8;
    --black: #111;
  }
  * { box-sizing: border-box; margin: 0; padding: 0; }
  html, body { width: 1199px; height: 1200px; overflow: hidden; background: var(--backdrop); }
  .letterhead {
    position: absolute; left: 159px; top: 30px; width: 881px; height: 1140px;
    background: var(--paper); font-family: "Montserrat", sans-serif; color: var(--ink);
    box-shadow: 0 4px 18px rgba(0,0,0,.18);
  }
  .brand {
    position: absolute; left: 71px; top: 62px; display: flex; align-items: center; gap: 10px;
    font-weight: 800; font-size: 38px; letter-spacing: -1px; color: var(--ink-dark);
  }
  .brand-square { width: 14px; height: 14px; background: var(--ink-dark); }
  .firm {
    position: absolute; left: 357px; top: 47px; font-size: 12px; line-height: 17.5px; text-transform: uppercase;
  }
  .firm-name { color: var(--brand-green); font-weight: 600; }
  .contact { position: absolute; left: 621px; top: 49px; list-style: none; font-size: 13px; line-height: 16.8px; text-transform: uppercase; }
  .contact li { display: flex; align-items: center; gap: 7px; }
  .contact svg { width: 10px; height: 10px; fill: var(--icon-cyan); }
  .salutation { position: absolute; left: 72px; top: 296px; font-family: "Pinyon Script", cursive; font-size: 27px; color: var(--black); }
  .body { position: absolute; left: 71px; top: 350px; width: 740px; font-size: 13.6px; line-height: 23px; text-align: justify; }
  .body p + p { margin-top: 23px; }
  .closing { position: absolute; left: 638px; top: 812px; font-family: "Tinos", serif; font-size: 15px; color: var(--black); line-height: 19px; }
  .signature { position: absolute; left: 621px; top: 830px; width: 150px; height: 72px; background: linear-gradient(100deg, rgba(35,80,200,.08), rgba(35,80,200,.18)); }
  .signer { position: absolute; left: 638px; top: 889px; font-family: "Tinos", serif; font-size: 15px; line-height: 19px; color: var(--black); }
  .signer em { font-style: italic; }
  .footer-band { position: absolute; left: 0; bottom: 0; width: 100%; height: 16px; display: flex; }
  .footer-band span { flex: 1; }
  .band-blue { background: var(--brand-blue); }
  .band-green { background: var(--brand-green); }
</style>
</head>
<body>
<main class="letterhead">
  <div class="brand"><span class="brand-square"></span>Brix2Key</div>

  <div class="firm">
    <div class="firm-name">Desmond R. Halvorsen IV,<br>Attorney at Law, PLLC</div>
    <div>2240 Larkspur Avenue Suite 300</div>
    <div>Dallas, Texas 75204</div>
  </div>

  <ul class="contact">
    <li><svg viewBox="0 0 10 10"><path d="M2 0.5 L3.8 2.6 L2.8 3.6 Q4 6 6.4 7.2 L7.4 6.2 L9.5 8 L8 9.5 Q1 8.5 0.5 2 Z"/></svg>(877) 555-0142</li>
    <li><svg viewBox="0 0 10 10"><rect x="2.5" y="0.5" width="5" height="3"/><rect x="0.5" y="3.5" width="9" height="4"/><rect x="2.5" y="6.5" width="5" height="3"/></svg>(469) 555-0187</li>
    <li><svg viewBox="0 0 10 10"><rect x="0.5" y="2" width="9" height="6" rx="1"/></svg>desk@brix2key.net</li>
    <li><svg viewBox="0 0 10 10"><circle cx="5" cy="5" r="4.5"/></svg>www.brix2key.com</li>
  </ul>

  <div class="salutation">Dear Smith</div>

  <section class="body">
    <p>Lorem ipsum dolor sit amet, consectetuer adipiscing elit, sed diam nonummy nibh euismod tincidunt ut laoreet dolore magna aliquam erat volutpat. Ut wisi enim ad minim veniam, quis nostrud exerci tation ullamcorper suscipit lobortis nisl ut aliquip ex ea commodo consequat. Duis autem vel eum iriure dolor in hendrerit in vulputate velit esse molestie consequat, vel illum dolore eu feugiat nulla facilisis at vero eros et accumsan et iusto odio dignissim qui blandit praesent luptatum zzril delenit augue duis dolore te feugait nulla facilisi.</p>
    <p>Lorem ipsum dolor sit amet, cons ectetuer adipiscing elit, sed diam nonummy nibh euismod tincidunt ut laoreet dolore magna aliquam erat volutpat. Ut wisi enim ad minim veniam, quis nostrud exerci tation ullamcorper suscipit lobortis nisl ut aliquip ex ea commodo consequat.</p>
    <p>Lorem ipsum dolor sit amet, consectetuer adipiscing elit, sed diam nonummy nibh euismod tincidunt ut laoreet dolore magna aliquam erat volutpat. Ut wisi enim ad minim veniam, quis nostrud exerci tation ullamcorper suscipit lobortis nisl ut aliquip ex ea commodo consequat. Duis autem vel eum iriure dolor in hendrerit in vulputate velit esse molestie consequat, vel illum dolore eu feugiat nulla facilisis at vero eros et accumsan et iusto odio dignissim qui blandit praesent luptatum zzril delenit augue duis dolore te feugait nulla facilisi.</p>
  </section>

  <div class="closing">Sincerely,</div>
  <div class="signature" role="img" aria-label="Handwritten signature of the attorney in blue ink"></div>
  <div class="signer">Desmond R. Halvorsen<br><em>Attorney at Law</em></div>

  <div class="footer-band"><span class="band-blue"></span><span class="band-green"></span></div>
</main>
</body>
</html>
```